Flyer for local business that installs fences and sells fence materials

We recently began selling fence materials, in addition to also doing fence installations. We need a flyer that displays our business information and photos of our work, as well as a flyer that shows customers they have the option to buy materials only also.

If they are looking to build a fence - we can help by installing it, or if they want to install themselves, they can buy the materials only from us too. We provide a lifetime warranty on all materials and installations. More information about the company is here: www.BrambleRailWorks.com

Its important to have the company logo, phone number, email and business hours listed (Monday - Thursday 9AM - 3PM, Friday 9AM - 1PM).

It is also important to show the fence material types we offer:
Wood, Chainlink, Vinyl and Aluminum
Updates

Updated with more photos and url to website www.bramblerailworks.com for details

Target Market(s)

Residential Homeowners

Industry/Entity Type

Construction

Font styles to use
Sans Serif
Other font styles liked:
• Arial

Colors
0054AA
0677BA
7BADD7
CADEEF
E8F1F8

Requirements
Must have
• Photos of the fencing we offer
Nice to have
• A way to explain to customers they can hire us to install, or just buy the materials from us
Should not have
• Too many colors or too many words

```html
<!DOCTYPE html>
<html lang="en">
<head>
<meta charset="utf-8">
<title>Bramble Rail Works Flyer</title>
<link href="https://fonts.googleapis.com/css2?family=Poppins:wght@400;500;600;700;800&display=swap" rel="stylesheet">
<style>
  :root {
    --blue: #3a83c9;
    --blue-dark: #2a6fb3;
    --brown: #5c4330;
    --orange: #f0932b;
    --red: #ee1c1c;
    --black: #050505;
    --ink: #111111;
    --white: #ffffff;
    --paper: #f1f1f1;
    --rule: #8a8a8a;
  }
  * { margin: 0; padding: 0; box-sizing: border-box; }
  html, body { width: 783px; height: 1200px; overflow: hidden; background: var(--paper); }
  body { position: relative; font-family: "Poppins", Arial, sans-serif; color: var(--ink); }

  .flyer {
    position: absolute; left: 21px; top: 121px;
    width: 806px; height: 1044px;
    transform: scale(0.918); transform-origin: top left;
    background: var(--white); overflow: hidden;
    box-shadow: 0 2px 8px rgba(0,0,0,.18);
  }

  .hero-photo {
    position: absolute; left: 0; top: 0; width: 806px; height: 520px;
    background:
      linear-gradient(180deg, #7ea6cf 0%, #b9cde0 22%, #c9c4b8 34%, #e7e6e0 44%, #cfcfcc 60%, #8b8a84 74%, #5a5140 88%, #4a3f2c 100%);
  }

  .brand { position: absolute; left: 270px; top: 44px; display: flex; align-items: flex-start; gap: 12px; }
  .brand-mark { width: 52px; height: 76px; background: var(--brown); margin-top: 2px; }
  .brand-name { font-weight: 700; font-size: 23px; line-height: 1; color: var(--blue); margin-top: 10px; }
  .brand-phone { font-weight: 700; font-size: 22px; line-height: 1.15; color: var(--ink); margin-top: 4px; }
  .brand-tagline { font-weight: 500; font-size: 7.5px; color: var(--ink); margin-top: 4px; }

  .headline {
    position: absolute; left: 77px; top: 380px; width: 651px; height: 140px;
    background: var(--blue); border-radius: 12px 12px 0 0;
    text-align: center; color: var(--white);
  }
  .headline-title { font-weight: 800; font-size: 63px; line-height: 1; margin-top: 20px; letter-spacing: -0.5px; }
  .headline-sub { font-weight: 700; font-size: 23px; line-height: 1; margin-top: 6px; }

  .features-band { position: absolute; left: 0; top: 500px; width: 806px; height: 141px; }
  .features {
    position: absolute; left: 0; top: 536px; width: 806px;
    display: grid; grid-template-columns: 146px 159px 205px 240px; column-gap: 0;
    padding-left: 62px; row-gap: 14px;
  }
  .feature { display: flex; gap: 7px; color: var(--white); font-weight: 600; font-size: 13px; line-height: 1.2; }
  .feature::before {
    content: ""; flex: none; width: 9px; height: 9px; margin-top: 3px;
    border-radius: 50%; background: var(--orange); box-shadow: inset 0 0 0 2px var(--orange), inset 0 0 0 3px #fff3;
  }

  .fence-types { position: absolute; left: 50px; top: 654px; display: flex; gap: 20px; }
  .fence-card { width: 162px; background: var(--white); box-shadow: 0 1px 4px rgba(0,0,0,.35); padding: 2px; }
  .fence-photo { height: 83px; }
  .fence-photo.wood { background: linear-gradient(90deg, #c79a5e, #e2bf87 50%, #b98c52); }
  .fence-photo.aluminum { background: linear-gradient(180deg, #e9ecef, #a9acae 55%, #7e7b74); }
  .fence-photo.vinyl { background: linear-gradient(180deg, #8fb0c8, #d9c7a3 45%, #6d7a3e); }
  .fence-photo.chain { background: linear-gradient(180deg, #b9c6cf, #d8dcdc 45%, #8c8f7d); }
  .fence-label { height: 30px; background: var(--orange); color: var(--white); font-weight: 600; font-size: 13px; text-align: center; line-height: 30px; }

  .estimates { position: absolute; left: 53px; top: 808px; width: 704px; height: 131px; border: 1px solid var(--rule); }
  .estimates-title {
    position: absolute; left: 130px; top: 786px; width: 545px; height: 42px;
    background: var(--red); border-radius: 14px; color: var(--white);
    font-weight: 800; font-size: 30px; line-height: 42px; text-align: center; letter-spacing: 0.3px;
  }
  .estimate-howto { position: absolute; left: 77px; top: 842px; width: 300px; font-size: 11.5px; font-weight: 600; line-height: 1.3; }
  .estimate-howto .online { color: var(--blue-dark); }
  .estimate-howto .virtual { color: var(--ink); margin-top: 13px; }
  .hours { position: absolute; left: 413px; top: 840px; width: 330px; }
  .hours-line { font-weight: 700; font-size: 17px; line-height: 1.25; }
  .hours-line .day { color: var(--blue); }
  .hours-note { font-size: 11.5px; line-height: 1.3; margin-top: 3px; width: 290px; }
  .hours-note .styles { color: var(--orange); font-weight: 600; }
  .social-square { position: absolute; left: 700px; top: 890px; width: 21px; height: 21px; background: var(--blue); border-radius: 3px; }

  .footer-shapes { position: absolute; left: 0; top: 0; }
  .call-now { position: absolute; left: 40px; top: 977px; font-weight: 700; font-size: 20px; color: var(--white); }
  .call-now .label { color: var(--orange); }
  .website { position: absolute; left: 440px; top: 988px; width: 340px; text-align: center; font-size: 19px; letter-spacing: 1.2px; color: var(--white); }
</style>
</head>
<body>
<main class="flyer">
  <div class="hero-photo" role="img" aria-label="Photo of a tall white vinyl privacy fence running along a backyard with houses behind"></div>

  <header class="brand">
    <div class="brand-mark"></div>
    <div>
      <div class="brand-name">Bramble Rail Works</div>
      <div class="brand-phone">555-014-2276</div>
      <div class="brand-tagline">"Because Good Fences Make Good Neighbors"</div>
    </div>
  </header>

  <section class="headline">
    <h1 class="headline-title">WE BUILD FENCES</h1>
    <p class="headline-sub">AND WE WOULD LOVE TO BUILD YOUR FENCE TOO!</p>
  </section>

  <svg class="features-band" viewBox="0 0 806 141" width="806" height="141" aria-hidden="true">
    <path d="M0 7 L8 15 L16 7 L24 15 L32 7 L40 15 L48 7 L56 15 L64 7 L72 15 L80 7 L88 15 L96 7 L104 15 L112 7 L120 15 L128 7 L136 15 L144 7 L152 15 L160 7 L168 15 L176 7 L184 15 L192 7 L200 15 L208 7 L216 15 L224 7 L232 15 L240 7 L248 15 L256 7 L264 15 L272 7 L280 15 L288 7 L296 15 L304 7 L312 15 L320 7 L328 15 L336 7 L344 15 L352 7 L360 15 L368 7 L376 15 L384 7 L392 15 L400 7 L408 15 L416 7 L424 15 L432 7 L440 15 L448 7 L456 15 L464 7 L472 15 L480 7 L488 15 L496 7 L504 15 L512 7 L520 15 L528 7 L536 15 L544 7 L552 15 L560 7 L568 15 L576 7 L584 15 L592 7 L600 15 L608 7 L616 15 L624 7 L632 15 L640 7 L648 15 L656 7 L664 15 L672 7 L680 15 L688 7 L696 15 L704 7 L712 15 L720 7 L728 15 L736 7 L744 15 L752 7 L760 15 L768 7 L776 15 L784 7 L792 15 L800 7 L806 13 L806 141 L0 141 Z" fill="var(--brown)"/>
    <polyline points="0,3 8,11 16,3 24,11 32,3 40,11 48,3 56,11 64,3 72,11 80,3 88,11 96,3 104,11 112,3 120,11 128,3 136,11 144,3 152,11 160,3 168,11 176,3 184,11 192,3 200,11 208,3 216,11 224,3 232,11 240,3 248,11 256,3 264,11 272,3 280,11 288,3 296,11 304,3 312,11 320,3 328,11 336,3 344,11 352,3 360,11 368,3 376,11 384,3 392,11 400,3 408,11 416,3 424,11 432,3 440,11 448,3 456,11 464,3 472,11 480,3 488,11 496,3 504,11 512,3 520,11 528,3 536,11 544,3 552,11 560,3 568,11 576,3 584,11 592,3 600,11 608,3 616,11 624,3 632,11 640,3 648,11 656,3 664,11 672,3 680,11 688,3 696,11 704,3 712,11 720,3 728,11 736,3 744,11 752,3 760,11 768,3 776,11 784,3 792,11 800,3 806,9" fill="none" stroke="var(--white)" stroke-width="2.5"/>
  </svg>

  <ul class="features" style="list-style:none">
    <li class="feature">Free<br>Estimates</li>
    <li class="feature">Concrete in<br>EVERY Post</li>
    <li class="feature">Lifetime Workmanship<br>Warranty</li>
    <li class="feature">Quality Workmanship<br>&amp; Materials</li>
    <li class="feature">Professional<br>Installation</li>
    <li class="feature">HOA Submission<br>Assistance</li>
    <li class="feature">Experienced Installation<br>TeamsAssistance</li>
    <li class="feature">FREE Gate Adjustments<br>for LIFE</li>
  </ul>

  <section class="fence-types">
    <figure class="fence-card"><div class="fence-photo wood" role="img" aria-label="Photo of a new wood privacy fence"></div><figcaption class="fence-label">Wood Fence</figcaption></figure>
    <figure class="fence-card"><div class="fence-photo aluminum" role="img" aria-label="Photo of wrapped aluminum fence materials on a pallet"></div><figcaption class="fence-label">Aluminum Fence</figcaption></figure>
    <figure class="fence-card"><div class="fence-photo vinyl" role="img" aria-label="Photo of a vinyl fence being installed in a yard"></div><figcaption class="fence-label">Vinyl Fence</figcaption></figure>
    <figure class="fence-card"><div class="fence-photo chain" role="img" aria-label="Photo of a chain link fence around a lawn"></div><figcaption class="fence-label">Chain Link Fence</figcaption></figure>
  </section>

  <section class="estimates"></section>
  <h2 class="estimates-title">ESTIMATES ARE ALWAYS FREE</h2>
  <div class="estimate-howto">
    <p class="online">Call, email, or message us online to<br>schedule an in-person estimate.</p>
    <p class="virtual">If you know your measurements OR have a lot<br>survey, email or call us for a virtual estimate!</p>
  </div>
  <div class="hours">
    <p class="hours-line"><span class="day">Monday - Thursday</span> 9AM - 3PM</p>
    <p class="hours-line"><span class="day">Friday</span> 9AM - 1PM</p>
    <p class="hours-note">Beautiful, professionally installed fences at affordable prices! <span class="styles">Many fence styles available.</span></p>
  </div>
  <div class="social-square"></div>

  <svg class="footer-shapes" viewBox="0 0 806 1044" width="806" height="1044" aria-hidden="true">
    <polygon points="0,952 345,952 420,1035 806,1035 806,1044 0,1044" fill="var(--black)"/>
    <polygon points="380,977 806,977 806,1030 425,1030" fill="var(--blue)"/>
  </svg>
  <p class="call-now"><span class="label">CALL US NOW:</span> 555-014-2276</p>
  <p class="website">www.bramblerailworks.com</p>
</main>
</body>
</html>
```